Morvell Electric Business Card

An electrical contractor needs a business card design, that will stand out.
I would like designs that use the colors in the logo shown. The logo attached I am ok with but if you have a better idea I am open for suggestions. I like the color scheme.
Industry/Entity Type
Electrical
Contact Information for Business Card
Services, social media, QR code,

```html
<!DOCTYPE html>
<html lang="en">
<head>
<meta charset="utf-8">
<title>Morvell Electric Business Card</title>
<link rel="stylesheet" href="https://fonts.googleapis.com/css2?family=Montserrat:wght@700;800&family=Arimo:wght@400;700&display=swap">
<style>
  :root {
    --page-bg: #2a2a2c;
    --card-bg: #1e1f21;
    --brand-yellow: #f2b705;
    --text-white: #ffffff;
    --rule: #bfbfbf;
    --deco-dark: #111213;
    --deco-light: #3a3c3f;
    --icon-ink: #1e1f21;
  }
  * { box-sizing: border-box; margin: 0; padding: 0; }
  html, body { width: 1200px; height: 1108px; overflow: hidden; }
  body {
    background: var(--page-bg);
    font-family: "Arimo", Arial, sans-serif;
    color: var(--text-white);
    display: flex;
    align-items: center;
    justify-content: center;
    gap: 80px;
  }
  .card {
    width: 420px;
    height: 700px;
    background: var(--card-bg);
    border-radius: 28px;
    position: relative;
    overflow: hidden;
    box-shadow: 0 18px 40px rgba(0,0,0,0.45);
    display: flex;
    flex-direction: column;
    align-items: center;
  }

  /* Front */
  .brand {
    margin-top: 110px;
    display: flex;
    align-items: center;
    gap: 14px;
  }
  .brand-square {
    width: 30px; height: 30px;
    background: var(--brand-yellow);
    border-radius: 6px;
  }
  .brand-name {
    font-family: "Montserrat", Arial, sans-serif;
    font-weight: 800;
    font-size: 30px;
    letter-spacing: 1px;
    color: var(--text-white);
    white-space: nowrap;
  }
  .person-name {
    margin-top: 70px;
    font-family: "Montserrat", Arial, sans-serif;
    font-weight: 700;
    font-size: 32px;
    color: var(--brand-yellow);
    letter-spacing: 0.5px;
  }
  .person-role {
    margin-top: 4px;
    font-size: 24px;
    color: var(--text-white);
  }
  .icon-row {
    margin-top: 16px;
    display: flex;
    align-items: center;
    gap: 10px;
    width: 340px;
  }
  .icon-row .rule { flex: 1; height: 1px; background: var(--rule); }
  .icon {
    width: 34px; height: 34px;
    background: var(--brand-yellow);
    border-radius: 7px;
    display: flex; align-items: center; justify-content: center;
  }
  .contact-list {
    margin-top: 22px;
    text-align: center;
    font-size: 24px;
    line-height: 1.25;
  }
  .divider { margin-top: 22px; width: 340px; height: 1px; background: var(--rule); }
  .address {
    margin-top: 20px;
    text-align: center;
    font-size: 24px;
    line-height: 1.25;
  }

  /* Back */
  .back-deco {
    margin-top: 70px;
    width: 320px; height: 320px;
    border-radius: 90px;
    background: linear-gradient(180deg, var(--deco-dark) 0%, var(--deco-dark) 40%, var(--deco-light) 100%);
  }
  .services-title {
    margin-top: 14px;
    font-family: "Arimo", Arial, sans-serif;
    font-weight: 700;
    font-size: 30px;
    color: var(--brand-yellow);
  }
  .services-list {
    list-style: none;
    margin-top: 10px;
    text-align: center;
    font-size: 18px;
    line-height: 1.35;
  }
  .services-list li::before {
    content: "";
    display: inline-block;
    width: 7px; height: 7px;
    border-radius: 50%;
    background: var(--brand-yellow);
    margin-right: 6px;
    vertical-align: middle;
    position: relative;
    top: -3px;
  }
</style>
</head>
<body>
  <section class="card card-front">
    <div class="brand">
      <span class="brand-square"></span>
      <span class="brand-name">MORVELL ELECTRIC</span>
    </div>
    <h1 class="person-name">DANIEL KERROW</h1>
    <p class="person-role">Manager</p>
    <div class="icon-row">
      <span class="rule"></span>
      <span class="icon" aria-label="Phone">
        <svg width="20" height="20" viewBox="0 0 24 24"><path d="M6.6 10.8a15 15 0 0 0 6.6 6.6l2.2-2.2a1 1 0 0 1 1-.25 11.4 11.4 0 0 0 3.6.57 1 1 0 0 1 1 1V20a1 1 0 0 1-1 1A17 17 0 0 1 3 4a1 1 0 0 1 1-1h3.5a1 1 0 0 1 1 1c0 1.25.2 2.45.57 3.57a1 1 0 0 1-.25 1z" fill="var(--icon-ink)"/></svg>
      </span>
      <span class="icon" aria-label="Email">
        <svg width="22" height="22" viewBox="0 0 24 24"><rect x="3" y="5" width="18" height="14" rx="1" fill="none" stroke="var(--icon-ink)" stroke-width="2"/><path d="M3 6l9 7 9-7" fill="none" stroke="var(--icon-ink)" stroke-width="2"/></svg>
      </span>
      <span class="icon" aria-label="Website">
        <svg width="22" height="22" viewBox="0 0 24 24"><circle cx="12" cy="12" r="9" fill="none" stroke="var(--icon-ink)" stroke-width="2"/><path d="M3 12h18M12 3c3 3 3 15 0 18M12 3c-3 3-3 15 0 18" fill="none" stroke="var(--icon-ink)" stroke-width="1.6"/></svg>
      </span>
      <span class="rule"></span>
    </div>
    <div class="contact-list">
      <p>555-218-7390</p>
      <p>hello@morvellmail.com</p>
      <p>www.morvellelec.com</p>
    </div>
    <div class="divider"></div>
    <div class="address">
      <p>27 Fenwick Road, Alder</p>
      <p>Ridge, ST 40213</p>
    </div>
  </section>

  <section class="card card-back">
    <div class="back-deco" role="img" aria-label="Large dark brand emblem decoration"></div>
    <h2 class="services-title">SERVICES</h2>
    <ul class="services-list">
      <li>Home Renovation electrical work</li>
      <li>Fixing of Faulty wiring</li>
      <li>Electrical Geyser Repair</li>
      <li>Installation of switchboards</li>
      <li>Tripping issues</li>
      <li>Repairing of outlets/fuses</li>
    </ul>
  </section>
</body>
</html>
```